Billboard Design

Billboard design featuring the colors dark teal and dark grey.
Company: Juniper Crest Holdings
Services Real Estate & Management
Phone: 717-390-6158
Important info:
Professionalizing Property Management
Specialized training and credentials in Property Management
Serving single family, multifamily, complexes, and mixed use properties.

UPDATE: We have uploaded photos from a recent project of ours and would love to see them used on the billboard.

```html
<!DOCTYPE html>
<html lang="en">
<head>
<meta charset="utf-8">
<title>Juniper Crest Holdings – Billboard</title>
<link rel="stylesheet" href="https://fonts.googleapis.com/css2?family=Crimson+Pro:wght@400;700&family=PT+Serif:wght@400&display=swap">
<style>
  :root {
    --teal: #00716f;
    --teal-line: #0a7b77;
    --grey-dark: #4a4a4a;
    --ink: #1b1b1b;
    --paper: #ffffff;
    --paper-soft: #f4f4f4;
    --stage-light: #8a8a8a;
    --stage-mid: #5e5e5e;
    --stage-dark: #3d3d3d;
  }
  html, body { margin: 0; padding: 0; width: 1056px; height: 1200px; overflow: hidden; }
  body {
    position: relative;
    background: linear-gradient(90deg, var(--stage-light), var(--stage-mid) 55%, var(--stage-dark));
  }
  .billboard {
    position: absolute; left: 48px; top: 450px;
    width: 960px; height: 300px;
    background: var(--paper);
    box-shadow: 0 14px 30px rgba(0,0,0,0.45);
  }
  .billboard svg { display: block; width: 960px; height: 300px; }
  .headline { font-family: "Crimson Pro", Georgia, serif; font-weight: 700; fill: var(--paper); font-size: 44px; }
  .brand-name { font-family: "Crimson Pro", Georgia, serif; font-weight: 400; fill: var(--grey-dark); font-size: 19px; }
  .benefit { font-family: "Crimson Pro", Georgia, serif; font-size: 17px; fill: var(--ink); }
  .phone-number { font-family: "PT Serif", Georgia, serif; font-size: 42px; fill: var(--ink); letter-spacing: 1px; }
  .tick { fill: none; stroke: var(--teal); stroke-width: 1.3; }
</style>
</head>
<body>
  <div class="billboard">
    <svg viewBox="0 0 960 300" xmlns="http://www.w3.org/2000/svg">
      <defs>
        <linearGradient id="hero-tones" x1="0" y1="0" x2="0" y2="1">
          <stop offset="0" stop-color="#c9d3d6"/>
          <stop offset="0.45" stop-color="#a9a197"/>
          <stop offset="0.75" stop-color="#5f8f3e"/>
          <stop offset="1" stop-color="#3f7a2a"/>
        </linearGradient>
      </defs>

      <rect class="hero-photo" x="0" y="0" width="560" height="230" fill="url(#hero-tones)" role="img" aria-label="Photo of a smiling couple in front of a suburban house with a green lawn"/>

      <path class="panel-edge" d="M496,0 C548,50 545,140 456,212 L560,212 L560,0Z" fill="var(--paper)"/>
      <path class="title-panel" d="M512,0 H960 V124 C880,104 760,100 690,108 C600,120 530,165 470,208 C545,140 560,55 512,0Z" fill="var(--teal)"/>
      <path class="accent-band" d="M470,208 C530,165 600,120 690,108 C760,100 880,104 960,124 V150 C880,124 760,114 690,120 C610,130 540,170 480,206Z" fill="var(--grey-dark)"/>

      <path class="info-band" d="M0,226 C120,180 300,168 480,200 C640,232 800,250 960,219 V300 H0Z" fill="var(--paper-soft)"/>
      <path class="info-band-edge" d="M0,226 C120,180 300,168 480,200 C640,232 800,250 960,219" fill="none" stroke="var(--teal-line)" stroke-width="4"/>

      <text class="headline" x="556" y="56">Real Estate &amp;</text>
      <text class="headline" x="926" y="100" text-anchor="end">Management</text>

      <g class="brand">
        <rect x="645" y="145" width="238" height="76" fill="none" stroke="var(--grey-dark)" stroke-width="2"/>
        <rect x="662" y="174" width="18" height="18" fill="var(--teal)"/>
        <text class="brand-name" x="690" y="189">Juniper Crest Holdings</text>
      </g>

      <g class="benefits">
        <g class="tick"><circle cx="53" cy="229" r="6.5"/><path d="M50,229 l2.3,2.3 l4,-4.6"/></g>
        <g class="tick"><circle cx="53" cy="252" r="6.5"/><path d="M50,252 l2.3,2.3 l4,-4.6"/></g>
        <g class="tick"><circle cx="53" cy="275" r="6.5"/><path d="M50,275 l2.3,2.3 l4,-4.6"/></g>
        <text class="benefit" x="67" y="234">Professionalizing Property Management</text>
        <text class="benefit" x="67" y="257">Specialized training and credentials in Property Management</text>
        <text class="benefit" x="67" y="280">Serving single family, multifamily, complexes, and mixed use properties.</text>
      </g>

      <g class="phone">
        <circle cx="615" cy="268" r="16" fill="none" stroke="var(--teal)" stroke-width="3"/>
        <path d="M608,259 c2,-2 4,-2 5,0 l2,4 c0.6,1.4 -0.4,2.2 -1.6,3 c1,2.6 2.6,4.4 5,5.6 c0.8,-1.2 1.8,-2.2 3,-1.6 l3.6,2 c1.6,1 1.4,3 -0.6,4.6 c-6,4 -18,-9 -15.4,-17.6z" fill="none" stroke="var(--teal)" stroke-width="2.2" stroke-linejoin="round"/>
        <text class="phone-number" x="646" y="284">717-390-6158</text>
      </g>
    </svg>
  </div>
</body>
</html>
```